Ravelor Global Kft. is an online recruitment marketplace connecting the employers and recruiters together. We provide an e-bussiness solution for companies and give busines opportunity for recruiters.
We have a logo design already, which should be used on the business card.
Our colours are grey and magenta, which can be seen in the logo. Black is also welcome.
The style should be dynamic, young but professional. It should be clear, visible, elegant, not too crowded, simple but exciting.
We need the following data on the BC: name, title, address, phone,fax and mobile number, email address, website.
Target Market(s)
Our target market are companies, as this is a B2B business. We also target recruiters, recruitment professionals, headhunters.We would like to be impressive and different.
Industry/Entity Type
Business
Requirements
Must have
- We would like to promote our website, www.ravelorglb.hu.
- Please, put this on the back with a quite visible letter size.The style should be dynamic, young but professional. It should be clear, visible, elegant, not too crowded, simple but exciting.
Should not have
- We do not want to see people figures.

```html
<!DOCTYPE html>
<html lang="en">
<head>
<meta charset="utf-8">
<title>Ravelor Global – business card options</title>
<link rel="stylesheet" href="https://fonts.googleapis.com/css2?family=Roboto+Slab:wght@400;700&display=swap">
<style>
  :root {
    --magenta: #b623b8;
    --violet-grey: #7b6c98;
    --ink: #5b4b78;
    --paper: #e8eae8;
    --box-soft: rgba(200, 200, 210, 0.55);
    --box-solid: #d9dbdb;
    --line: #3a3a3a;
  }
  html, body {
    margin: 0;
    width: 921px;
    height: 1200px;
    overflow: hidden;
    background: #fff;
  }
  body {
    position: relative;
    font-family: "Roboto Slab", Georgia, serif;
  }
  .column-label {
    position: absolute;
    top: 0;
    font: 400 15px Arial, Helvetica, sans-serif;
    color: #222;
  }
  .column-label.front { left: 168px; }
  .column-label.back { left: 602px; }

  .card {
    position: absolute;
    height: 252px;
    border: 1px solid var(--line);
    overflow: hidden;
    box-sizing: border-box;
  }
  .card.front { left: 8px; width: 448px; }
  .card.back { left: 488px; width: 430px; }

  .puzzle-field {
    position: absolute;
    inset: 0;
    background: linear-gradient(135deg, var(--magenta) 0%, var(--violet-grey) 55%, var(--magenta) 100%);
  }
  .card.back .puzzle-field { bottom: 38%; }

  .name-box {
    position: absolute;
    left: 9%;
    top: 38%;
    width: 70%;
    height: 32%;
    display: flex;
    align-items: center;
    justify-content: center;
    background: var(--box-soft);
  }
  .name-box.solid {
    left: 15%;
    width: 64%;
    top: 32%;
    height: 32%;
    background: var(--box-solid);
    border: 2px solid #f4f4f4;
    box-sizing: border-box;
  }
  .brand-name {
    font-weight: 700;
    font-size: 32px;
    color: var(--magenta);
    white-space: nowrap;
  }

  .info-band {
    position: absolute;
    left: 0; right: 0; bottom: 0;
    height: 38%;
    background: var(--paper);
  }
  .holder {
    position: absolute;
    left: 6%;
    top: 30%;
  }
  .holder-name {
    font-weight: 700;
    font-size: 17px;
    color: var(--ink);
    margin: 0;
  }
  .holder-role {
    font-weight: 700;
    font-style: italic;
    font-size: 10px;
    color: var(--magenta);
    margin: 2px 0 0 62px;
  }
  .contacts {
    position: absolute;
    left: 51%;
    top: 8%;
    margin: 0;
    padding: 0;
    list-style: none;
    font-weight: 700;
    font-size: 10.5px;
    line-height: 15.5px;
    color: var(--ink);
    white-space: nowrap;
  }
  .contacts b { color: var(--magenta); margin-right: 4px; }
</style>
</head>
<body>
  <span class="column-label front">front of card</span>
  <span class="column-label back">back of card</span>

  <!-- Option 1 -->
  <section class="card front" style="top:25px">
    <div class="puzzle-field" role="img" aria-label="Interlocking jigsaw pieces in magenta and grey-violet"></div>
    <div class="name-box"><span class="brand-name">Ravelor Global</span></div>
  </section>
  <section class="card back" style="top:25px">
    <div class="puzzle-field" role="img" aria-label="Interlocking jigsaw pieces in magenta and grey-violet"></div>
    <div class="info-band">
      <div class="holder"><p class="holder-name">PROJECT OWNER</p><p class="holder-role">owner or position</p></div>
      <ul class="contacts">
        <li><b>A.</b>PO Box 1024, City, Zipcode</li>
        <li><b>P.</b>(06) 555-0142</li>
        <li><b>F.</b>(06) 555-0187</li>
        <li><b>@.</b>hello@ravelorglb.hu</li>
        <li><b>W.</b>www.ravelorglb.hu</li>
      </ul>
    </div>
  </section>

  <!-- Option 2 -->
  <section class="card front" style="top:323px">
    <div class="puzzle-field" role="img" aria-label="Interlocking jigsaw pieces in magenta and grey-violet"></div>
    <div class="name-box"><span class="brand-name">Ravelor Global</span></div>
  </section>
  <section class="card back" style="top:323px">
    <div class="puzzle-field" role="img" aria-label="Interlocking jigsaw pieces in magenta and grey-violet"></div>
    <div class="info-band">
      <div class="holder"><p class="holder-name">PROJECT OWNER</p><p class="holder-role">owner or position</p></div>
      <ul class="contacts">
        <li><b>A.</b>PO Box 1024, City, Zipcode</li>
        <li><b>P.</b>(06) 555-0142</li>
        <li><b>F.</b>(06) 555-0187</li>
        <li><b>@.</b>hello@ravelorglb.hu</li>
        <li><b>W.</b>www.ravelorglb.hu</li>
      </ul>
    </div>
  </section>

  <!-- Option 3 -->
  <section class="card front" style="top:620px">
    <div class="puzzle-field" role="img" aria-label="Interlocking jigsaw pieces in magenta and grey-violet"></div>
    <div class="name-box solid"><span class="brand-name">Ravelor Global</span></div>
  </section>
  <section class="card back" style="top:620px">
    <div class="puzzle-field" role="img" aria-label="Interlocking jigsaw pieces in magenta and grey-violet"></div>
    <div class="info-band">
      <div class="holder"><p class="holder-name">PROJECT OWNER</p><p class="holder-role">owner or position</p></div>
      <ul class="contacts">
        <li><b>A.</b>PO Box 1024, City, Zipcode</li>
        <li><b>P.</b>(06) 555-0142</li>
        <li><b>F.</b>(06) 555-0187</li>
        <li><b>@.</b>hello@ravelorglb.hu</li>
        <li><b>W.</b>www.ravelorglb.hu</li>
      </ul>
    </div>
  </section>

  <!-- Option 4 -->
  <section class="card front" style="top:918px">
    <div class="puzzle-field" role="img" aria-label="Interlocking jigsaw pieces in magenta and grey-violet"></div>
    <div class="name-box solid"><span class="brand-name">Ravelor Global</span></div>
  </section>
  <section class="card back" style="top:918px">
    <div class="puzzle-field" role="img" aria-label="Interlocking jigsaw pieces in magenta and grey-violet"></div>
    <div class="info-band">
      <div class="holder"><p class="holder-name">PROJECT OWNER</p><p class="holder-role">owner or position</p></div>
      <ul class="contacts">
        <li><b>A.</b>PO Box 1024, City, Zipcode</li>
        <li><b>P.</b>(06) 555-0142</li>
        <li><b>F.</b>(06) 555-0187</li>
        <li><b>@.</b>hello@ravelorglb.hu</li>
        <li><b>W.</b>www.ravelorglb.hu</li>
      </ul>
    </div>
  </section>
</body>
</html>
```